Design refresh required for educational resources

A full redesign/refresh is required for an education resource kit.
The final outputs will include:
- Powerpoint slide template
- parent handout template
- overview template
- 2 different types of lesson plan templates (can be related but need to have some differences to distinguish between the two)
- 2 x branded labels for resources
- teacher 'intervention plan' summary sheet
- 'scope and sequence' document
Design needs to have a fun, modern feel, capturing elements of the New Zealand landscape, flora and/or fauna.
The resources will be used as part of a teaching kit for use in schools.
Please see attached files for existing samples of some of the above documents. Full content to be provided for successful applicant.
Please submit sample of one or two of the documents to bid for this work - enough so that I can see the overall design aesthetic you are proposing.
New Zealand teachers and parents of 5 year old children

```html
<!DOCTYPE html>
<html lang="en">
<head>
<meta charset="utf-8">
<title>Week One Overview and Intervention Plan</title>
<link href="https://fonts.googleapis.com/css2?family=Boogaloo&family=Amatic+SC:wght@700&family=Lobster&family=Lobster+Two:ital,wght@1,700&family=Montserrat:wght@400;600;700&display=swap" rel="stylesheet">
<style>
:root{
  --backdrop:#8f9095;
  --maroon:#6b0f2f;
  --ink:#3a3a3a;
  --sky:#5fd0f5;
  --blue:#29a9e0;
  --purple:#a2368d;
  --green:#7bb142;
  --yellow:#f0c94d;
  --teal:#1aa6b2;
  --coral:#dd7567;
  --rose:#a77b73;
  --mint:#c6e8da;
  --t-week:#3fa9de;
  --t-book:#b04a9a;
  --t-sound:#8cc04a;
  --t-read:#f2c94c;
  --t-words:#36b6c4;
  --t-vocab:#e57f6f;
}
*{box-sizing:border-box;margin:0;padding:0}
html,body{width:975px;height:1200px;overflow:hidden}
body{background:var(--backdrop);position:relative;font-family:'Montserrat',sans-serif;color:var(--ink)}
.page{position:absolute;width:399px;height:565px;overflow:hidden;box-shadow:0 6px 10px rgba(0,0,0,.25)}
.page--kids{left:73px;top:21px;background:#fff}
.page--photo{left:503px;top:21px;width:398px;height:563px}
.page--plan{left:288px;top:607px;width:398px;height:563px}

/* shared brand name */
.brand{position:absolute;display:flex;align-items:center;gap:5px;font-family:'Montserrat',sans-serif;font-weight:700;font-size:7px;line-height:1;color:var(--maroon);white-space:nowrap}
.brand__mark{width:8px;height:8px;background:var(--maroon)}

/* kids page */
.kids__sky{position:absolute;left:0;top:0;width:100%;height:140px;background:linear-gradient(180deg,var(--sky) 0%,#a6e4f8 60%,#fff 100%)}
.kids__cloud{position:absolute;right:0;top:0;width:170px;height:70px;background:#fff;border-radius:0 0 0 60px}
.kids__ground{position:absolute;left:0;bottom:0;width:100%;height:130px;background:linear-gradient(180deg,#fff 0%,var(--mint) 45%,var(--mint) 100%);border-radius:60% 40% 0 0/20% 20% 0 0}
.kids__bird{position:absolute;left:32px;top:68px;width:88px;height:80px;border-radius:50% 45% 40% 50%;background:radial-gradient(circle at 50% 40%,#9bb83a,#7e9d2c)}
.kids__friends{position:absolute;left:5px;top:445px;width:385px;height:120px;background:linear-gradient(90deg,rgba(79,183,184,.55),rgba(143,181,52,.45) 40%,rgba(232,140,110,.35) 70%,rgba(125,80,50,.45));border-radius:40px 40px 0 0;opacity:.6}
.badge-week{position:absolute;left:29px;top:17px;width:105px;height:41px;background:#fff;border-radius:7px;font-family:'Boogaloo',sans-serif;color:var(--maroon);font-size:23px;display:flex;align-items:center;justify-content:center}
.kids__title{position:absolute;left:126px;top:99px;font-family:'Boogaloo',sans-serif;font-weight:400;color:var(--maroon);font-size:50px;line-height:1}
.kids .brand{left:290px;top:38px}
.tag{position:absolute;left:36px;width:106px;height:27px;color:#fff;font-family:'Amatic SC',sans-serif;font-weight:700;font-size:11.5px;line-height:1.05;padding:3px 10px;display:flex;align-items:center}
.tag--book{top:164px;background:var(--blue)}
.tag--vocab{top:194px;background:var(--purple)}
.tag--phon{top:224px;background:var(--green)}
.tag--pic{top:255px;background:var(--yellow)}
.tag--read{top:305px;background:var(--teal)}
.tag--mat{top:355px;background:var(--coral)}

.info{position:absolute;font-size:8.6px;line-height:1.25}
.info p{margin-bottom:4px}
.rule{position:absolute;height:0;border-top:1px dashed #9a9a9a}
.checks{list-style:none}
.checks li{position:relative;padding-left:13px;margin-bottom:10px}
.checks li svg{position:absolute;left:0;top:1px;width:8px;height:8px}

/* photo page */
.photo__bg{position:absolute;inset:0;background:
  linear-gradient(180deg,rgba(255,255,255,0) 0%,rgba(255,255,255,.85) 30%,rgba(255,255,255,.95) 55%,rgba(255,255,255,.6) 75%,rgba(255,255,255,0) 100%),
  linear-gradient(180deg,#cdb8a2 0%,#e7b8c8 20%,#e9d8e6 45%,#d9d3ea 70%,#8c7cc3 90%,#7a9a5a 100%)}
.pill-week{position:absolute;left:0;top:25px;width:171px;height:53px;background:var(--rose);border-radius:0 27px 27px 0;font-family:'Lobster',cursive;color:#fff;font-size:26px;display:flex;align-items:center;padding-left:28px}
.photo__title{position:absolute;left:0;width:100%;top:102px;text-align:center;font-family:'Lobster',cursive;font-weight:400;color:var(--maroon);font-size:48px;line-height:1}
.photo .brand{left:290px;top:48px}
.label{position:absolute;left:38px;font-family:'Lobster Two',cursive;font-style:italic;font-weight:700;font-size:9px;line-height:1.3;color:#2b2b2b}

/* plan page */
.plan__bg{position:absolute;inset:0;background:
  linear-gradient(180deg,rgba(255,255,255,0) 0%,rgba(255,255,255,.25) 20%,rgba(255,255,255,.55) 45%,rgba(255,255,255,.35) 70%,rgba(255,255,255,0) 100%),
  linear-gradient(180deg,#8e8a63 0%,#a6a27a 12%,#c9c2a6 30%,#d9d5c8 55%,#c7cbb9 75%,#b9b997 88%,#8a9552 100%)}
.plan__title{position:absolute;left:28px;top:44px;font-family:'Lobster',cursive;font-weight:400;color:#fff;font-size:26px;line-height:1}
.plan .brand{left:276px;top:58px}
.plan-table{position:absolute;left:28px;top:80px;width:341px;display:grid;grid-template-columns:repeat(6,1fr);grid-template-rows:46px repeat(9,45.7px);font-size:5.4px;line-height:1.2;text-align:center}
.plan-table .th{font-family:'Boogaloo',sans-serif;color:#fff;font-size:10px;line-height:1.1;display:flex;align-items:center;justify-content:center}
.plan-table .td{display:flex;flex-direction:column;align-items:center;justify-content:center;gap:5px;padding:2px 3px;border-top:1px solid rgba(255,255,255,.7);border-right:1px solid rgba(255,255,255,.7)}
.th.c1{background:var(--t-week)}.th.c2{background:var(--t-book)}.th.c3{background:var(--t-sound)}
.th.c4{background:var(--t-read)}.th.c5{background:var(--t-words)}.th.c6{background:var(--t-vocab)}
.td.c1{background:rgba(216,236,248,.75);font-size:10px}
.td.c2{background:rgba(244,224,240,.7);font-weight:700}
.td.c3{background:rgba(232,244,218,.7);font-size:9px;letter-spacing:.5px}
.td.c4{background:rgba(252,244,214,.7)}
.td.c5{background:rgba(214,240,244,.7)}
.td.c6{background:rgba(250,226,222,.7)}
</style>
</head>
<body>

<!-- Illustrated overview -->
<section class="page page--kids kids">
  <div class="kids__sky" role="img" aria-label="Blue sky with sun rays and white clouds"></div>
  <div class="kids__cloud"></div>
  <div class="kids__ground" role="img" aria-label="Green meadow with bush, mushrooms and flowers"></div>
  <div class="kids__bird" role="img" aria-label="Illustrated green kākāpō flapping a wing"></div>
  <div class="kids__friends" role="img" aria-label="Illustrated kākāpō, kiwi, bush, ferns and toadstools on a hill"></div>

  <div class="badge-week">Week One</div>
  <div class="brand"><span class="brand__mark"></span>Kōwhai Reading Kit</div>
  <h1 class="kids__title">Overview</h1>

  <div class="tag tag--book">Book</div>
  <div class="tag tag--vocab">Vocabulary target words from story</div>
  <div class="tag tag--phon">Target phonemes and graphemes</div>
  <div class="tag tag--pic">Target picture card words</div>
  <div class="tag tag--read">Readers</div>
  <div class="tag tag--mat">Materials for games</div>

  <div class="info" style="left:176px;top:169px">The Night Walk of Ruru and Kiwi<br>by Jane Morton and Lucy Fenwick</div>
  <div class="rule" style="left:176px;width:190px;top:195px"></div>
  <div class="info" style="left:176px;top:201px">velvety, decorate, marama (moon), rākau (tree)</div>
  <div class="rule" style="left:176px;width:190px;top:225px"></div>
  <div class="info" style="left:176px;top:230px">M m and D d</div>
  <div class="rule" style="left:176px;width:190px;top:255px"></div>
  <div class="info" style="left:176px;top:261px"><p>dog, dam, dot, den, dig</p><p>mat, mop, map, men, mud</p><p>marama, manu, moe</p></div>
  <div class="rule" style="left:176px;width:190px;top:305px"></div>
  <div class="info" style="left:176px;top:311px"><p>CV CVC VC words with short vowels</p><p>Easier: Tip, Tap; Pip in the Pot</p><p>Harder: Dot and Mim; Mud on Dad</p></div>
  <div class="rule" style="left:176px;width:190px;top:355px"></div>
  <ul class="info checks" style="left:176px;top:362px;width:195px">
    <li><svg viewBox="0 0 10 10"><circle cx="5" cy="5" r="4.2" fill="none" stroke="#c0405a" stroke-width="1"/><path d="M3 5l1.6 1.6L8.5 2" fill="none" stroke="#c0405a" stroke-width="1"/></svg>Large d and m letter cards: lower case and upper case</li>
    <li><svg viewBox="0 0 10 10"><circle cx="5" cy="5" r="4.2" fill="none" stroke="#c0405a" stroke-width="1"/><path d="M3 5l1.6 1.6L8.5 2" fill="none" stroke="#c0405a" stroke-width="1"/></svg>Target picture cards: d and m (picture one side, word reverse side)</li>
    <li><svg viewBox="0 0 10 10"><circle cx="5" cy="5" r="4.2" fill="none" stroke="#c0405a" stroke-width="1"/><path d="M3 5l1.6 1.6L8.5 2" fill="none" stroke="#c0405a" stroke-width="1"/></svg>Segmentation boards and counters</li>
    <li><svg viewBox="0 0 10 10"><circle cx="5" cy="5" r="4.2" fill="none" stroke="#c0405a" stroke-width="1"/><path d="M3 5l1.6 1.6L8.5 2" fill="none" stroke="#c0405a" stroke-width="1"/></svg>‘Special container’ to place words in for phoneme identity game</li>
    <li><svg viewBox="0 0 10 10"><circle cx="5" cy="5" r="4.2" fill="none" stroke="#c0405a" stroke-width="1"/><path d="M3 5l1.6 1.6L8.5 2" fill="none" stroke="#c0405a" stroke-width="1"/></svg>White board and marker</li>
  </ul>
</section>

<!-- Photographic overview -->
<section class="page page--photo photo">
  <div class="photo__bg" role="img" aria-label="Soft-focus photo of pink sweet pea flowers with a white butterfly above a field of purple lupins"></div>
  <div class="pill-week">Week One</div>
  <div class="brand"><span class="brand__mark"></span>Kōwhai Reading Kit</div>
  <h1 class="photo__title">Overview</h1>

  <div class="label" style="top:180px">Book</div>
  <div class="label" style="top:209px">Vocabulary target words<br>from story</div>
  <div class="label" style="top:240px">Target phonemes and<br>graphemes</div>
  <div class="label" style="top:272px">Target picture card words</div>
  <div class="label" style="top:322px">Readers</div>
  <div class="label" style="top:373px">Materials for games</div>

  <div class="info" style="left:175px;top:181px">The Night Walk of Ruru and Kiwi<br>by Jane Morton and Lucy Fenwick</div>
  <div class="rule" style="left:38px;width:328px;top:206px"></div>
  <div class="info" style="left:175px;top:212px">velvety, decorate, marama (moon), rākau (tree)</div>
  <div class="rule" style="left:38px;width:328px;top:237px"></div>
  <div class="info" style="left:175px;top:242px">M m and D d</div>
  <div class="rule" style="left:38px;width:328px;top:267px"></div>
  <div class="info" style="left:175px;top:273px"><p>dog, dam, dot, den, dig</p><p>mat, mop, map, men, mud</p><p>marama, manu, moe</p></div>
  <div class="rule" style="left:38px;width:328px;top:317px"></div>
  <div class="info" style="left:175px;top:323px"><p>CV CVC VC words with short vowels</p><p>Easier: Tip, Tap; Pip in the Pot</p><p>Harder: Dot and Mim; Mud on Dad</p></div>
  <div class="rule" style="left:38px;width:328px;top:367px"></div>
  <ul class="info checks" style="left:175px;top:374px;width:195px">
    <li><svg viewBox="0 0 10 10"><circle cx="5" cy="5" r="4.2" fill="none" stroke="#c0405a" stroke-width="1"/><path d="M3 5l1.6 1.6L8.5 2" fill="none" stroke="#c0405a" stroke-width="1"/></svg>Large d and m letter cards: lower case and upper case</li>
    <li><svg viewBox="0 0 10 10"><circle cx="5" cy="5" r="4.2" fill="none" stroke="#c0405a" stroke-width="1"/><path d="M3 5l1.6 1.6L8.5 2" fill="none" stroke="#c0405a" stroke-width="1"/></svg>Target picture cards: d and m (picture one side, word reverse side)</li>
    <li><svg viewBox="0 0 10 10"><circle cx="5" cy="5" r="4.2" fill="none" stroke="#c0405a" stroke-width="1"/><path d="M3 5l1.6 1.6L8.5 2" fill="none" stroke="#c0405a" stroke-width="1"/></svg>Segmentation boards and counters</li>
    <li><svg viewBox="0 0 10 10"><circle cx="5" cy="5" r="4.2" fill="none" stroke="#c0405a" stroke-width="1"/><path d="M3 5l1.6 1.6L8.5 2" fill="none" stroke="#c0405a" stroke-width="1"/></svg>‘Special container’ to place words in for phoneme identity game</li>
    <li><svg viewBox="0 0 10 10"><circle cx="5" cy="5" r="4.2" fill="none" stroke="#c0405a" stroke-width="1"/><path d="M3 5l1.6 1.6L8.5 2" fill="none" stroke="#c0405a" stroke-width="1"/></svg>White board and marker</li>
  </ul>
</section>

<!-- Intervention plan -->
<section class="page page--plan plan">
  <div class="plan__bg" role="img" aria-label="Photo of a kea parrot in alpine tussock at the top and sheep grazing in a green paddock at the bottom"></div>
  <h1 class="plan__title">Intervention Plan</h1>
  <div class="brand"><span class="brand__mark"></span>Kōwhai Reading Kit</div>

  <div class="plan-table">
    <div class="th c1">Week</div><div class="th c2">Book</div><div class="th c3">Target<br>Sounds</div><div class="th c4">Suggested<br>Readers</div><div class="th c5">Target<br>Words</div><div class="th c6">Vocabulary</div>

    <div class="td c1">1</div><div class="td c2">Night Walk of Ruru and Kiwi</div><div class="td c3">m d</div>
    <div class="td c4"><span>Tip, Tap Pip in the Pot</span><span>Dot and Mim Mud on Dad</span></div>
    <div class="td c5"><span>mop, mat, mad, map, men dog, dig, dad, dot, den</span><span>marama, manu, moe</span></div>
    <div class="td c6">velvety decorate marama (moon) rākau (tree)</div>

    <div class="td c1">2</div><div class="td c2">Tuna in the Creek</div><div class="td c3">p t</div>
    <div class="td c4"><span>Tip, Tap Pip in the Pot</span><span>Tam's Pan Pip's Pet</span></div>
    <div class="td c5"><span>pot, pet, pan, pen, pod tap, top, ten, ted, tag</span><span>pahi, pā, tuna</span></div>
    <div class="td c6">glistened reflection pō (night) tuna (eel)</div>

    <div class="td c1">3</div><div class="td c2">Cat on the Hill</div><div class="td c3">c l</div>
    <div class="td c4"><span>Ben and the Bug Nat in a Net</span><span>A Cup for Pip Dot and the Cap</span></div>
    <div class="td c5"><span>cat, cap, cot, cup, cut lid, lip, leg, lab, log</span></div>
    <div class="td c6">howl roam ngeru (cat) hīkoi (walk)</div>

    <div class="td c1">4</div><div class="td c2">Koro and the Bellbird</div><div class="td c3">n b</div>
    <div class="td c4"><span>Ben and the Bug Nat in a Net</span><span>Bat Has a Nap Pip and Big Ted</span></div>
    <div class="td c5"><span>nap, nut, nun, nan, net bat, bug, bun, bin, bed</span><span>niho, noke, noho</span></div>
    <div class="td c6">whisper nectar waiata (song) tamariki (children)</div>

    <div class="td c1">5</div><div class="td c2">Piwi the Fantail Takes Flight</div><div class="td c3">s f<br>*blends</div>
    <div class="td c4"><span>Rat on a Rug</span><span>Dot the Fat Cat Frog in the Fern Fin the Mudfish</span></div>
    <div class="td c5"><span>sun, stop, spot, stamp, split fish, frog, flag, flip, frost</span></div>
    <div class="td c6">fidget ruckus kōhanga (nest) awhina (help)</div>

    <div class="td c1">6</div><div class="td c2">Koro and the Rainbow</div><div class="td c3">g r</div>
    <div class="td c4"><span>Rat on a Rug</span><span>Rat Can Ride Run, Ruru, Run Fun in the Sun</span></div>
    <div class="td c5"><span>gum, gran, grape, gate, green rat, rug, rope, rake, ramp</span><span>roto, rā, rama</span></div>
    <div class="td c6">laid beg tino pai (great job) uenuku (rainbow)</div>

    <div class="td c1">7</div><div class="td c2">Weka Sings</div><div class="td c3">w h</div>
    <div class="td c4"><span>Wet Weka</span><span>Hen and the Bee</span></div>
    <div class="td c5"><span>web, wing, wake, wink, weed hat, hen, hand, hive, hit</span><span>waha, waka, hipi</span></div>
    <div class="td c6">carefully drift aroha (love) mokopuna (grandchildren)</div>

    <div class="td c1">8</div><div class="td c2">Kiwi Digs for Bugs</div><div class="td c3">sh k</div>
    <div class="td c4"><span>Weka and the Shed</span><span>A Windy Day</span></div>
    <div class="td c5"><span>ship, shed, shake, shrub, sheep kit, kick, kid, kiss, kilt</span><span>koko, kura, kākā</span></div>
    <div class="td c6">locate scrumptious kai (food) kōawa (stream)</div>

    <div class="td c1">9&amp;10</div><div class="td c2">Teacher's choice</div><div class="td c3">ch, v th, j</div>
    <div class="td c4"><span>Chip and Chat Van to the Vet Bug in the Jug</span><span>The Lost Chick Jen Has Spots</span></div>
    <div class="td c5">Teacher's choice</div>
    <div class="td c6">Teacher's choice</div>
  </div>
</section>

</body>
</html>
```